Design a label for a dog shampoo names furbloom, the sell point of this series of shampoo is “just like wash your dogs with milk, not harm for your hand ”, the style could be gentle or professional or even amazing.

Use only 2 colors in the design job, the color of our logo could be changed, it depends on your whole page. Please design in CDR or ai.

update:
Pls do more change with the fonts when you design the front page, including title and details. Try more styles of fonts. Addition, this design will be printed on the bottle, no a label stick on it.
Updates

Do not put a real dog or animal on the page, Pay more attention to the types of fonts

Reason: Expect for more design idea.

Target Market(s)

people 20-30 years old who have dogs and cats at home

Industry/Entity Type

It Professional

Requirements
Nice to have
• It would be nice if you add some detail words in the design of the right side.

```html
<!DOCTYPE html>
<html lang="en">
<head>
<meta charset="UTF-8">
<title>Furbloom Shampoo Label</title>
<link rel="stylesheet" href="https://fonts.googleapis.com/css2?family=Lilita+One&family=Arimo:wght@400;700&display=swap">
<style>
  :root {
    --pink: #d9579c;
    --pink-soft: #f3c6dd;
    --orange: #ef8262;
    --white: #ffffff;
    --backdrop: #e7e8e9;
  }
  html, body { margin: 0; padding: 0; overflow: hidden; }
  body { width: 1200px; height: 846px; background: var(--backdrop); }
  .canvas { position: relative; width: 1200px; height: 846px; overflow: hidden; }

  .label {
    position: absolute; top: 94px; width: 343px; height: 657px;
    border-radius: 22px; overflow: hidden; background: var(--white);
    box-shadow: 0 2px 8px rgba(0,0,0,0.12);
  }
  .label--front { left: 214px; }
  .label--back { left: 644px; }

  /* front */
  .front-ornament-top {
    position: absolute; left: 0; top: 0; width: 100%; height: 118px;
    background: linear-gradient(180deg, var(--pink) 0%, var(--pink) 62%, var(--pink-soft) 100%);
  }
  .front-ornament-bottom {
    position: absolute; left: 0; bottom: 0; width: 100%; height: 122px;
    background: linear-gradient(0deg, var(--pink) 0%, var(--pink) 70%, var(--pink-soft) 100%);
  }
  .brand {
    position: absolute; left: 0; top: 122px; width: 100%; text-align: center;
    font-family: "Lilita One", sans-serif; font-size: 32px; color: var(--orange);
    line-height: 1;
  }
  .title {
    position: absolute; left: 0; top: 174px; width: 100%; margin: 0;
    text-align: center; font-family: "Lilita One", sans-serif; font-weight: 400;
    font-size: 30px; line-height: 46px; color: var(--orange);
    white-space: nowrap; letter-spacing: -0.3px;
    transform: scaleY(1.25); transform-origin: top center;
  }
  .paw-icon {
    position: absolute; left: 112px; top: 290px; width: 120px; height: 118px;
    border-radius: 50%; background: var(--pink);
  }
  .tagline {
    position: absolute; left: 0; top: 426px; width: 100%; margin: 0;
    text-align: center; font-family: "Arimo", sans-serif; font-weight: 700;
    font-size: 13.5px; line-height: 16px; color: var(--pink);
  }
  .benefits {
    position: absolute; left: 0; top: 474px; width: 100%; margin: 0;
    text-align: center; font-family: "Arimo", sans-serif; font-weight: 700;
    font-size: 18.5px; line-height: 24px; color: var(--orange);
  }
  .volume {
    position: absolute; left: 0; bottom: 22px; width: 100%; text-align: center;
    font-family: "Arimo", sans-serif; font-weight: 700; font-size: 27px;
    color: var(--white); letter-spacing: 0.5px;
  }

  /* back */
  .back-ornament-top {
    position: absolute; left: 0; top: 0; width: 100%; height: 62px;
    background: linear-gradient(180deg, var(--pink-soft) 0%, var(--white) 100%);
  }
  .back-ornament-bottom {
    position: absolute; left: 0; bottom: 0; width: 100%; height: 74px;
    background: linear-gradient(0deg, var(--pink-soft) 0%, var(--white) 100%);
  }
  .details {
    position: absolute; left: 29px; top: 66px; width: 287px;
    font-family: "Arimo", sans-serif; font-size: 12.4px; line-height: 13.2px;
    color: var(--pink); text-align: justify;
  }
  .details p { margin: 0 0 12px; }
  .details ul { margin: 0 0 12px; padding: 0; list-style: none; text-align: left; }
  .details li::before { content: "\2022\00a0"; }
  .details .lead, .details .heading { color: var(--orange); font-weight: 700; }
  .details .heading-block { display: block; }
</style>
</head>
<body>
<div class="canvas">

  <section class="label label--front">
    <div class="front-ornament-top" role="img" aria-label="Pink swirl ornament border"></div>
    <div class="brand">furbloom</div>
    <h1 class="title">SUPER-CONDITIONING<br>&amp; NUTRIENT SHAMPOO</h1>
    <div class="paw-icon" role="img" aria-label="Pink paw print icon"></div>
    <p class="tagline">just like wash your dogs with milk,<br>not harm for your hand</p>
    <p class="benefits">MOISTURE-RICH<br>SMOOTH AND SILKY</p>
    <div class="front-ornament-bottom" role="img" aria-label="Pink swirl ornament border"></div>
    <div class="volume">1000 ML</div>
  </section>

  <section class="label label--back">
    <div class="back-ornament-top" role="img" aria-label="Pink swirl ornament border"></div>
    <div class="details">
      <p><span class="lead">FURBLOOM Super-Conditioning &amp; Nutrient Shampoo</span> is a specially formulated shampoo, rich in conditioners picked up from milk which subdivide and balance nutrition of pet's coat. More easier and better assimilate for coat from base to the end after using. With the help of minus-ion, the balancer of nutrition, rinses out quickly and completely to leave a soft, sparkling, and smooth coat. Safe and gentle enough to be used every day. Safe for even the most sensitive skin and coat, puppies, lactating bitches and cats.</p>
      <span class="heading heading-block">DERECTIONS:</span>
      <ul>
        <li>Before shampooing, blush out pet's coat.</li>
        <li>Saturate dog's coat with lukewarm water.</li>
        <li>Dispense a small amount of shampoo into the palm of your hand.</li>
        <li>To clean coat, start at dog's head and work back towards the tail. Avoid getting shampoo into the dog's eyes and ears.</li>
        <li>Rinse coat sereral times with lukewarm water.</li>
        <li>Towel dry and gently comb or brush coat.</li>
      </ul>
      <p><span class="heading">ACTIVE INGREDIENTS:</span> Hypochlorous Acid, Sodium Hypochlorite</p>
      <p><span class="heading">USE PRECAUTIONS:</span> Harmful if swallowed. Do not inhale. Discontinue use if irritation develops and contact your veterinarian. For animal use only. Not for human use. Keep out of reach of children. Do not decant into smaller containers. Not for injection. Always consult with a Veterinarian for systemic conditions.</p>
      <p><span class="heading">STORAGE AND DISPOSAL:</span> Keep out of the tough of children. Replace Cap. Wrap in several layers of newspaper and discard in trash.</p>
    </div>
    <div class="back-ornament-bottom" role="img" aria-label="Pink swirl ornament border"></div>
  </section>

</div>
</body>
</html>
```